Brighten Your Compass - book web site

I need a web site for my book that is being published and will be available on Zorvel April 6th. It will have an email opt in which will then email the person a pdf report.
And it will have a bio page.
My logo, pic, book cover and bio details are attached below.

Target Market(s)

New life coaches that are looking to figure out their purpose and branding for their business

Industry/Entity Type

Life Coaching

Number of Pages Required

3 page

Font styles to use
Serif

Requirements
Must have
• The book cover, my logo, an opt in page, a bio page, my picture
• i would like the book in the header
• Needs to be chatterloop compliant
Should not have
• except for the logo, tranquil heart and soul will NOT be highlighted in the header

```html
<!DOCTYPE html>
<html lang="en">
<head>
<meta charset="utf-8">
<title>Brighten Your Compass</title>
<link href="https://fonts.googleapis.com/css2?family=Lora:wght@400;700&family=Open+Sans:wght@400;600&display=swap" rel="stylesheet">
<style>
:root{
  --accent:#9b1c1c;
  --brand:#d9481c;
  --gold:#f2b01e;
  --ink:#222;
  --body:#444;
  --muted:#888;
  --line:#d9d9d9;
  --field:#f4f4f4;
  --footer:#333;
  --white:#fff;
}
*{box-sizing:border-box;margin:0;padding:0}
html,body{width:1200px;height:3072px;overflow:hidden}
body{position:relative;background:var(--white);font-family:"Open Sans",Arial,sans-serif;color:var(--body)}

/* header */
.site-header{position:absolute;left:0;top:0;width:1200px;height:118px;background:var(--white)}
.logo{position:absolute;left:133px;top:44px;display:flex;align-items:center;gap:10px}
.logo-dot{width:26px;height:26px;border-radius:50%;background:var(--gold)}
.logo-name{font-family:"Lora",Georgia,serif;font-weight:700;font-size:20px;color:var(--brand);text-transform:uppercase;letter-spacing:.5px}
.main-nav{position:absolute;right:133px;top:52px;display:flex;gap:28px;font-size:12px;text-transform:uppercase}
.main-nav a{color:var(--ink);text-decoration:none}
.main-nav a.active{color:var(--accent)}

/* hero */
.hero{position:absolute;left:0;top:118px;width:1200px;height:496px}
.hero-photo{position:absolute;inset:0;
  background:linear-gradient(180deg,#7fc4dc 0%,#d5e9ef 45%,#e6dcc4 78%,#d9a23e 100%)}
.hero-arrow{position:absolute;top:228px;width:40px;height:40px;border-radius:50%;background:rgba(120,120,120,.55)}
.hero-arrow.prev{left:25px}.hero-arrow.next{right:25px}
.hero-arrow svg{position:absolute;left:12px;top:11px}
.hero-copy{position:absolute;left:657px;top:140px;width:420px}
.hero-title{font-family:"Lora",Georgia,serif;font-size:38px;font-weight:400;color:var(--ink);line-height:1.2;white-space:nowrap}
.hero-text{margin-top:18px;font-size:11.5px;line-height:19px;color:var(--ink)}
.btn-buy{margin-top:22px;display:inline-flex;align-items:center;gap:8px;height:46px;padding:0 24px;background:var(--gold);
  font-family:"Lora",Georgia,serif;font-weight:700;font-size:15px;color:var(--ink);text-transform:uppercase}

/* content sections */
.section-title{font-family:"Lora",Georgia,serif;font-weight:400;font-size:43px;color:var(--accent)}
.copy{width:613px;font-size:12.4px;line-height:23px;color:var(--body);text-align:justify}
.copy p+p{margin-top:22px}
.about{position:absolute;left:133px;top:700px}
.about .copy{margin-top:18px}
.retailer{margin-top:12px;font-size:22px;font-weight:600;color:var(--ink);letter-spacing:-.5px}
.book-cover{position:absolute;left:786px;top:713px;width:281px;height:417px;
  background:linear-gradient(160deg,#5fae9d 0%,#3f8d7f 55%,#2f6e64 100%)}

.band{position:absolute;left:0;width:1200px;height:319px;text-align:center}
.band-one{top:1229px;background:linear-gradient(90deg,#7b6a55 0%,#b8a48a 45%,#a08b70 70%,#6b5a48 100%)}
.band-two{top:2245px;background:linear-gradient(90deg,#8a7d62 0%,#b7ab8c 50%,#8f6e58 80%,#5a4535 100%)}
.band-heading{position:absolute;left:0;width:100%;top:118px;font-family:"Lora",Georgia,serif;font-size:33px;color:var(--white)}
.band-link{position:absolute;left:0;width:100%;top:170px;font-family:"Lora",Georgia,serif;font-size:16px;color:var(--white);text-decoration:underline;text-transform:uppercase}

.bio{position:absolute;left:133px;top:1612px}
.bio .copy{margin-top:22px}
.portrait{position:absolute;left:786px;top:1628px;width:281px;height:416px;
  background:linear-gradient(180deg,#c8c8c4 0%,#8a6a58 45%,#3a2c28 100%)}

/* contact */
.contact{position:absolute;left:133px;top:2628px}
.contact-email{margin-top:22px;font-size:16px;color:var(--ink)}
.social{position:absolute;left:133px;top:2748px;display:flex;gap:22px}
.social-item{display:flex;flex-direction:column;align-items:center;gap:4px}
.social-item span.box{width:42px;height:42px;background:#8a8a8a}
.social-item span.label{font-size:9px;color:var(--muted)}
.field{position:absolute;height:42px;border:1px solid var(--line);background:var(--field);font-size:11px;color:var(--muted);padding:13px 20px}
.btn-submit{position:absolute;left:608px;top:2826px;width:90px;height:41px;background:var(--footer);color:var(--white);
  font-family:"Lora",Georgia,serif;font-size:12px;text-transform:uppercase;display:flex;align-items:center;justify-content:center}

/* footer */
.site-footer{position:absolute;left:0;top:2935px;width:1200px;height:137px;background:var(--footer);text-align:center;color:#bbb;font-size:11px}
.footer-nav{position:absolute;top:46px;width:100%}
.footer-nav a{color:#ddd;text-decoration:none;margin:0 8px}
.copyright{position:absolute;top:76px;width:100%}
</style>
</head>
<body>

<header class="site-header">
  <div class="logo"><span class="logo-dot"></span><span class="logo-name">Tranquil Heart and Soul</span></div>
  <nav class="main-nav">
    <a class="active" href="#">Home</a><a href="#">Bio</a><a href="#">Buy Now</a><a href="#">Contact</a>
  </nav>
</header>

<section class="hero">
  <div class="hero-photo" role="img" aria-label="Photo of a woman in a white dress leaping on a sunny beach"></div>
  <div class="hero-arrow prev"><svg width="14" height="18" viewBox="0 0 14 18"><path d="M11 2 L3 9 L11 16" fill="none" stroke="#fff" stroke-width="3"/></svg></div>
  <div class="hero-arrow next"><svg width="14" height="18" viewBox="0 0 14 18"><path d="M3 2 L11 9 L3 16" fill="none" stroke="#fff" stroke-width="3"/></svg></div>
  <div class="hero-copy">
    <h1 class="hero-title">Brighten Your Compass</h1>
    <p class="hero-text">Aliquam erat volutpat. Proin eget sodales ipsum, et lacinia dolor. Sed pharetra enim eu gravida dignissim. Vivamus purus nisl, ornare ac interdum ac, cursus sed magna. Donec quis tortor pulvinar dolor auctor consectetur.</p>
    <div class="btn-buy"><svg width="16" height="14" viewBox="0 0 16 14"><path d="M0 1h3l2 8h8l2-6H4" fill="none" stroke="#222" stroke-width="1.8"/><circle cx="6" cy="12" r="1.4" fill="#222"/><circle cx="12" cy="12" r="1.4" fill="#222"/></svg>Buy Now</div>
  </div>
</section>

<section class="about">
  <h2 class="section-title">About Book</h2>
  <div class="copy">
    <p>Mauris laoreet velit quis ex feugiat vestibulum. Proin non dapibus elit. Fusce sit amet mi a nunc consectetur dictum id consectetur felis. Vivamus aliquet posuere elit id porttitor. Nullam euismod tempor urna, quis laoreet nunc interdum eget. Aliquam justo metus, accumsan at dui eget, consequat ullamcorper est. Pellentesque ante diam, mollis sed euismod sit amet, posuere eget risus. Nulla in quam consectetur quam convallis pellentesque at vel est. Vivamus interdum sem vitae iaculis tincidunt. Nam mattis nunc id ex bibendum accumsan. Vestibulum convallis elementum volutpat. Donec nulla massa, malesuada at gravida pellentesque, dignissim imperdiet ex. In eget cursus purus, ac efficitur sapien.</p>
    <p>Maecenas vel molestie felis, nec sollicitudin odio. Mauris nec lacinia sem. Cras in ipsum id mauris pulvinar porttitor et a velit. Sed sed augue id tortor tempus pulvinar ut a orci. Donec eget euismod quam. Nam in lobortis purus. Cras arcu nisi, dapibus id eros vitae, sagittis faucibus lectus. Suspendisse leo augue, congue eu molestie in, rutrum eu purus. Sed mollis condimentum dui, et ultricies leo luctus lobortis. Proin molestie tincidunt bibendum.</p>
  </div>
  <div class="retailer">Zorvel</div>
</section>
<div class="book-cover" role="img" aria-label="Book cover: Brighten Your Compass, with a magnifying glass on a teal background"></div>

<section class="band band-one" role="img" aria-label="Photo of hands holding small paper slips with handwritten notes">
  <div class="band-heading">Nulla diam purus, molestie vitae lacus</div>
  <div class="band-link">Read More</div>
</section>

<section class="bio">
  <h2 class="section-title">Bio</h2>
  <div class="copy">
    <p>Marla Quennell, founder of Tranquil Heart and Soul, helps new coaches and creative entrepreneurs find their inner voice so that they have the confidence to bring their authentic selves out into the world.</p>
    <p>Marla's keen sense of what works is backed by a thorough education in psychology, health, nutrition, training and management. She's a certified health counselor, having trained at the Institute for Whole-Food Coaching in New York (accredited by Ridgefield Teachers College).</p>
    <p>She holds a bachelor's degree in psychology from Harborview University, giving her a deep understanding of the motivations behind food, career and lifestyle choices. She spent a decade in management with some of the most successful food businesses in the country.</p>
    <p>Marla has helped businesses achieve dramatic improvements in their organization and focus – in turn, making their businesses more profitable. Clients who seek Marla's guidance are ready to get real and get wise, both in terms of health and business goals. She helps coaches quickly recognize easy to integrate strategies that will suit their work style to help eliminate the confusion on what to do next which in turn will boost their confidence and their bottom line.</p>
    <p>Marla is a classically trained culinary chef from Calloway Culinary University and a certified raw foods chef, a certified yoga instructor, reiki master, an RestWell facilitator, and a certified Business Coach for Wellness and Artistic Professionals.</p>
  </div>
</section>
<div class="portrait" role="img" aria-label="Portrait photo of the author"></div>

<section class="band band-two" role="img" aria-label="Photo of a woman with eyes closed in soft warm light">
  <div class="band-heading">Integer in elit at ipsum imperdiet euismod</div>
  <div class="band-link">Read More</div>
</section>

<section class="contact">
  <h2 class="section-title">Contact Us</h2>
  <p class="contact-email">Email : info@marlaquennell.com</p>
</section>
<div class="social">
  <div class="social-item"><span class="box"></span><span class="label">chatterloop</span></div>
  <div class="social-item"><span class="box"></span><span class="label">pinboardly</span></div>
  <div class="social-item"><span class="box"></span><span class="label">chirpnest</span></div>
  <div class="social-item"><span class="box"></span><span class="label">circleplus</span></div>
</div>
<div class="field" style="left:608px;top:2716px;width:224px">Name</div>
<div class="field" style="left:844px;top:2716px;width:223px">Email</div>
<div class="field" style="left:608px;top:2771px;width:459px">Name</div>
<div class="btn-submit">Submit</div>

<footer class="site-footer">
  <div class="footer-nav"><a href="#">Home</a>|<a href="#">Bio</a>|<a href="#">Buy Now</a>|<a href="#">Contact</a></div>
  <div class="copyright">Copyright © 2017 Company name. All rights reserved.</div>
</footer>

</body>
</html>
```